Website art for a private investigator.

The purposed graphic is for a business website ( dorvelgrp.example ). The business name is “Dorvale & Kestrin ltd.” This firm is a private investigation agency. The purposed graphic will be placed in the upper most main area of the main page of the website. If you look at the website now there is no graphic.

I have an idea of what I am looking for. I imagine a graphic depicting a contemporary private investigator walking through a dark alley searching for some unknown item. This is symbolic of private investigators hired to find information for people who their selfs do not have the know how nor could they handle the complexity and high stress environment. When I say contemporary I am referring to todays private investigators typically highly educated and well dressed.

Target Market(s)

People who need a private investigator

Industry/Entity Type

Business

Requirements
Must have
• match website; I have an idea of what I am looking for. I imagine a graphic depicting a contemporary private investigator walking through a dark alley searching for some unknown item. This is symbolic of private investigators hired to find information for people who their selfs do not have the know how nor could they handle the complexity and high stress environment. When I say contemporary I am referring to todays private investigators typically highly educated and well dressed.
Should not have
• Everyone please understand, I am not looking for a new website. I am only looking for the image. If you have submitted a design and its displayed on another website other than mine. I will not select your design. I am sorry for being harsh, but I asked for the image to match my website.

```html
<!DOCTYPE html>
<html lang="en">
<head>
<meta charset="utf-8">
<title>Dorvale &amp; Kestrin ltd. — Private Investigation and Analysis</title>
<link rel="stylesheet" href="https://fonts.googleapis.com/css2?family=Montserrat:wght@400;500;600&family=Lato:ital,wght@0,400;0,700;1,400;1,700&display=swap">
<style>
  :root {
    --page: #ffffff;
    --ink: #222222;
    --body-ink: #444444;
    --quote-mark: #c8c8c8;
    --link: #2a3f8f;
    --link-soft: #8a8a8a;
    --hero-deep: #05080c;
    --hero-mid: #1f3d56;
    --hero-light: #4d7898;
    --social-bar: #121416;
    --button-top: #2b8cf0;
    --button-bottom: #0a5fcf;
    --button-edge: #0a4aa8;
    --white: #ffffff;
  }
  * { margin: 0; padding: 0; box-sizing: border-box; }
  html, body { width: 1200px; height: 900px; overflow: hidden; background: var(--page); }
  body { position: relative; font-family: "Lato", Arial, sans-serif; color: var(--ink); }
  a { text-decoration: none; }

  .hero { position: absolute; left: 50px; top: 56px; width: 1100px; height: 159px; overflow: hidden; }
  .hero-image {
    position: absolute; inset: 0;
    background:
      linear-gradient(90deg, rgba(5,8,12,.75) 0%, rgba(5,8,12,0) 25%, rgba(5,8,12,0) 75%, rgba(5,8,12,.7) 100%),
      linear-gradient(180deg, var(--hero-light) 0%, var(--hero-mid) 45%, #0f1f2c 75%, var(--hero-deep) 100%);
  }
  .social-bar { position: absolute; left: 0; top: 0; width: 230px; height: 34px; background: var(--social-bar); display: flex; align-items: center; gap: 21px; padding-left: 22px; }
  .social-dot { width: 12px; height: 12px; border-radius: 50%; background: var(--white); opacity: .85; }
  .main-nav { position: absolute; left: 252px; top: 12px; font-family: "Lato", Arial, sans-serif; font-size: 8px; }
  .main-nav a { position: absolute; color: var(--white); white-space: nowrap; }
  .main-nav .n-main { left: 0; opacity: .75; }
  .main-nav .n-invest { left: 40px; }
  .main-nav .n-news { left: 139px; }
  .main-nav .n-fees { left: 179px; }
  .hero-title, .hero-tagline { position: absolute; left: 273px; font-family: "Montserrat", Arial, sans-serif; font-weight: 600; font-size: 12.5px; color: var(--white); white-space: nowrap; }
  .hero-title { top: 58px; }
  .hero-tagline { top: 91px; }

  .contact-phone { position: absolute; left: 670px; top: 232px; font-family: "Montserrat", Arial, sans-serif; font-size: 12.5px; font-weight: 500; color: var(--ink); }
  .request-button { position: absolute; left: 672px; top: 258px; width: 117px; height: 20px; border-radius: 10px; background: linear-gradient(180deg, var(--button-top), var(--button-bottom)); border: 1px solid var(--button-edge); color: var(--white); font-family: "Lato", Arial, sans-serif; font-weight: 700; font-size: 7.5px; display: flex; align-items: center; justify-content: center; }

  .section-title { position: absolute; left: 323px; font-family: "Montserrat", Arial, sans-serif; font-weight: 400; color: var(--ink); white-space: nowrap; }
  .section-title.intro { top: 315px; font-size: 16px; }
  .section-title.what { top: 706px; font-size: 12.5px; }

  .quote-mark { position: absolute; font-family: "Lato", Arial, sans-serif; font-style: italic; font-size: 46px; line-height: 1; color: var(--quote-mark); }
  .quote-text { position: absolute; left: 327px; font-family: "Lato", Arial, sans-serif; font-style: italic; font-size: 9.3px; line-height: 15.2px; color: var(--ink); }
  .quote-text.lead { font-weight: 700; width: 525px; top: 368px; }
  .quote-text.review-a { width: 545px; top: 472px; }
  .quote-text.review-b { width: 530px; top: 575px; }
  .quote-credit { position: absolute; right: 327px; font-size: 6.2px; color: var(--ink); font-family: "Lato", Arial, sans-serif; white-space: nowrap; }

  .service-copy { position: absolute; left: 323px; width: 555px; font-family: Arial, Helvetica, sans-serif; font-size: 7.3px; line-height: 15px; color: var(--body-ink); }
  .service-copy .accent { color: var(--link); }
  .service-copy .muted { color: var(--link-soft); }
</style>
</head>
<body>
  <header class="hero">
    <div class="hero-image" role="img" aria-label="Header photograph: a contemporary, well-dressed private investigator walking through a dark, misty alley at night, searching under street lamps"></div>
    <div class="social-bar" aria-label="Social links">
      <span class="social-dot"></span><span class="social-dot"></span><span class="social-dot"></span>
      <span class="social-dot"></span><span class="social-dot"></span><span class="social-dot"></span>
    </div>
    <nav class="main-nav">
      <a class="n-main" href="#">Main</a>
      <a class="n-invest" href="#">Investigation &amp; Analysis</a>
      <a class="n-news" href="#">News</a>
      <a class="n-fees" href="#">Fees</a>
    </nav>
    <h1 class="hero-title">Dorvale &amp; Kestrin ltd.</h1>
    <p class="hero-tagline">A Private Investigation and Analysis Firm</p>
  </header>

  <p class="contact-phone">Tel. (740) 555-0142</p>
  <a class="request-button" href="#">Submit Request For Service</a>

  <h2 class="section-title intro">Ohio and West Virginia Private Investigators</h2>

  <span class="quote-mark" style="left:323px;top:343px;">“</span>
  <p class="quote-text lead">Our experience and unbiased approach is your greatest strength! If you are an attorney, company, or private individual with a legal need we will provide you with accurate, timely and unbiassed information that will help you make an informed decision, mitigate risk, and resolve problems.</p>
  <span class="quote-mark" style="left:826px;top:411px;">”</span>

  <span class="quote-mark" style="left:323px;top:448px;">“</span>
  <p class="quote-text review-a">Dorvale &amp; Kestrin, Ltd. have been very helpful in our requests. Callum is a very courteous and respectful person. Thanks for all you have done thus far!!! We will definitely use this firm in the future!!</p>
  <p class="quote-credit" style="top:506px;">— Harlan T. Brevick, Jr., Attorney at Law, Brevick Law Office - South Point, Ohio</p>
  <span class="quote-mark" style="left:855px;top:514px;">”</span>

  <span class="quote-mark" style="left:323px;top:550px;">“</span>
  <p class="quote-text review-b">Our Union recently hired Dorvale and Kestrin to conduct an investigation for us. The investigation concerned a certain high ranking official. The investigation entailed researching retrospectively over a course of several years. We found that Dorvale and Kestrin conducted a very thorough and accurate account of the information as requested. The report we were given was very professional, concise and satisfied our needs. The investigation was carried out and completed in a timely fashion assuring our union of the information we needed without undue costs.</p>
  <p class="quote-credit" style="top:654px;">— Renee Albright, President Federal Workers Local 4187</p>
  <span class="quote-mark" style="left:855px;top:663px;">”</span>

  <h3 class="section-title what">What We Do</h3>

  <p class="service-copy" style="top:733px;"><span class="accent">Dorvale</span> &amp; Kestrin' <span class="accent">private investigators</span> are available for immediate service in <span class="accent">Ohio</span> throughout the cities of <span class="accent">Ironton</span>, <span class="accent">Portsmouth</span>, <span class="accent">Gallipolis</span>, <span class="accent">Jackson</span>, <span class="accent">Chillicothe</span>, <span class="accent">Cincinnati</span>, <span class="accent">Columbus</span>, and surrounding areas. Service is immediately available in <span class="accent">West Virginia</span> throughout the cities of <span class="accent">Huntington</span>, <span class="accent">Charleston</span>, and surrounding areas.</p>

  <p class="service-copy" style="top:778px;">Private investigators are available to provide full support to attorneys involved in <span class="muted">criminal defense</span> and <span class="muted">civil litigation</span>. Full investigative support is available to the general public involving <span class="accent">criminal</span> and <span class="accent">civil matters</span>.</p>

  <p class="service-copy" style="top:823px;"><span class="accent">Dorvale</span> &amp; Kestrin <span class="accent">private investigators</span> are always easily obtainable for the general public. We keep our fee's reasonable and never <span class="accent">charge</span> for travel. This makes us available to you without unnecessary expense. Investigative and analysis services are available by the <span class="accent">hour</span> or for a flat rate. <span class="muted">Click here for our Fees</span>.</p>
</body>
</html>
```